CD Cover Design - Islamic Hadith CD

Hi,

I need a design for CD cover. The title is Echoes of Brightwater(p.b.u.h)

Front + Back + Round CD

Its a CD with stories/Hadith describing prophet Tavrenal(p.b.u.h)

The CD is for Kids and contains stories narrated by children from around the globe.

I want the look to be really cool, inspirational and bright.

I am NOT looking for Islamic themed designs.

This what I want the cover to say

Front
Title - Echoes of Brightwater(saws)
A few moments of remembering the Prophet(saws)

Authentic Ahadith's about the Prophet(p.b.u.h)
Presented by Children from around the world.

Source: Velqoni, Darvet, Quorlesa

Logo(with website address and FB)

Back
A unique presentatio by the cildren from around the world for their brother and sisters in Islam
For more info about our courses and programs visit www.kitebrightlearn.com. Find us on [url removed, login to view]

Track list
title, name

```html
<!DOCTYPE html>
<html lang="en">
<head>
<meta charset="utf-8">
<title>Echoes of Brightwater – CD Cover and Disc</title>
<link rel="stylesheet" href="https://fonts.googleapis.com/css2?family=PT+Sans+Narrow:wght@400;700&family=PT+Sans:wght@400;700&display=swap">
<style>
  :root {
    --paper: #ffffff;
    --backdrop: #f1f1f3;
    --title-purple: #6a3c9c;
    --brand-purple: #7a2f8f;
    --tagline-blue: #1e8fd0;
    --source-grey: #8a8a8a;
    --disc-rim: #d9d9de;
    --hole: #f1f1f3;
    --wave-orange: #f59a1b;
    --wave-yellow: #f7d21e;
    --wave-green: #7cc242;
    --wave-blue: #1ea3dc;
    --wave-magenta: #d6259a;
    --wave-pink: #f06bb5;
  }
  html, body {
    margin: 0;
    padding: 0;
    width: 1200px;
    height: 1030px;
    overflow: hidden;
    background: var(--backdrop);
  }
  .canvas {
    position: relative;
    width: 1200px;
    height: 1030px;
  }

  /* Front cover */
  .front-cover {
    position: absolute;
    left: 40px;
    top: 235px;
    width: 560px;
    height: 560px;
    background: var(--paper);
    box-shadow: 0 2px 10px rgba(0,0,0,0.12);
    overflow: hidden;
  }
  .cover-title {
    position: absolute;
    right: 34px;
    top: 40px;
    margin: 0;
    text-align: right;
    font-family: "PT Sans Narrow", sans-serif;
    font-weight: 700;
    font-size: 38px;
    line-height: 1.0;
    color: var(--title-purple);
  }
  .cover-subtitle {
    position: absolute;
    right: 34px;
    top: 122px;
    margin: 0;
    font-family: "PT Sans Narrow", sans-serif;
    font-weight: 700;
    font-size: 17px;
    color: var(--title-purple);
  }
  .brand {
    position: absolute;
    display: flex;
    align-items: center;
    gap: 6px;
    font-family: "PT Sans Narrow", sans-serif;
    font-weight: 700;
    color: var(--brand-purple);
  }
  .brand-dot {
    border-radius: 50%;
    background: var(--brand-purple);
  }
  .front-cover .brand { left: 22px; top: 90px; font-size: 20px; }
  .front-cover .brand-dot { width: 12px; height: 12px; }

  .wave-art {
    position: absolute;
    left: 0;
    top: 150px;
    width: 560px;
    height: 280px;
  }
  .cover-tagline {
    position: absolute;
    left: 0;
    right: 0;
    top: 448px;
    margin: 0;
    text-align: center;
    font-family: "PT Sans", sans-serif;
    font-weight: 700;
    font-size: 17px;
    line-height: 1.3;
    color: var(--tagline-blue);
  }
  .cover-sources {
    position: absolute;
    left: 0;
    right: 0;
    top: 505px;
    margin: 0;
    text-align: center;
    font-family: "PT Sans", sans-serif;
    font-size: 13px;
    color: var(--source-grey);
  }

  /* Disc label */
  .disc-label {
    position: absolute;
    left: 640px;
    top: 255px;
    width: 520px;
    height: 520px;
  }
  .disc-title {
    position: absolute;
    left: 0;
    right: 0;
    top: 62px;
    margin: 0;
    text-align: center;
    font-family: "PT Sans Narrow", sans-serif;
    font-weight: 700;
    font-size: 34px;
    line-height: 1.0;
    color: var(--title-purple);
  }
  .disc-subtitle {
    position: absolute;
    left: 0;
    right: 0;
    top: 138px;
    margin: 0;
    text-align: center;
    font-family: "PT Sans Narrow", sans-serif;
    font-weight: 700;
    font-size: 15px;
    color: var(--title-purple);
  }
  .disc-label .brand { left: 380px; top: 208px; font-size: 18px; }
  .disc-label .brand-dot { width: 10px; height: 10px; }
</style>
</head>
<body>
<main class="canvas">

  <section class="front-cover" aria-label="Front cover">
    <h1 class="cover-title">Echoes of<br>Brightwater (saws)</h1>
    <p class="cover-subtitle">A few moments of remembering the Prophet (saws)</p>

    <div class="brand"><span class="brand-dot"></span>Kitebright</div>

    <svg class="wave-art" viewBox="0 0 560 280" role="img" aria-label="Colourful rainbow wave with swirling curls sweeping across the cover">
      <defs>
        <linearGradient id="cover-wave" x1="0" y1="1" x2="1" y2="0">
          <stop offset="0" stop-color="var(--wave-green)"/>
          <stop offset="0.25" stop-color="var(--wave-yellow)"/>
          <stop offset="0.45" stop-color="var(--wave-orange)"/>
          <stop offset="0.65" stop-color="var(--wave-magenta)"/>
          <stop offset="0.85" stop-color="var(--wave-blue)"/>
          <stop offset="1" stop-color="var(--wave-pink)"/>
        </linearGradient>
      </defs>
      <path d="M0 250 C120 140 200 60 330 40 C430 25 510 40 560 60 L560 120 C480 95 400 100 330 140 C250 190 170 250 110 280 L0 280 Z" fill="url(#cover-wave)" opacity="0.9"/>
    </svg>

    <p class="cover-tagline">Authentic Ahadith's about the Prophet (p.b.u.h)<br>Presented by Children from around the world.</p>
    <p class="cover-sources">Source: Velqoni, Darvet, Quorlesa</p>
  </section>

  <section class="disc-label" aria-label="Disc label">
    <svg width="520" height="520" viewBox="0 0 520 520" style="position:absolute;left:0;top:0">
      <defs>
        <clipPath id="disc-clip"><circle cx="260" cy="260" r="258"/></clipPath>
        <linearGradient id="disc-wave" x1="0" y1="0" x2="1" y2="1">
          <stop offset="0" stop-color="var(--wave-magenta)"/>
          <stop offset="0.3" stop-color="var(--wave-blue)"/>
          <stop offset="0.55" stop-color="var(--wave-orange)"/>
          <stop offset="0.75" stop-color="var(--wave-yellow)"/>
          <stop offset="1" stop-color="var(--wave-green)"/>
        </linearGradient>
      </defs>
      <circle cx="260" cy="260" r="258" fill="var(--paper)" stroke="var(--disc-rim)" stroke-width="2"/>
      <g clip-path="url(#disc-clip)">
        <path d="M0 250 C100 220 200 250 300 300 C380 340 460 330 520 300 L520 520 L0 520 Z" fill="url(#disc-wave)" opacity="0.9" role="img" aria-label="Colourful rainbow wave with swirling curls across the lower disc"/>
      </g>
      <circle cx="260" cy="260" r="62" fill="none" stroke="var(--disc-rim)" stroke-width="2"/>
      <circle cx="260" cy="260" r="22" fill="var(--hole)" stroke="var(--disc-rim)" stroke-width="2"/>
    </svg>
    <h2 class="disc-title">Echoes of<br>Brightwater (saws)</h2>
    <p class="disc-subtitle">A few moments of remembering the Prophet (saws)</p>
    <div class="brand"><span class="brand-dot"></span>Kitebright</div>
  </section>

</main>
</body>
</html>
```